Etiketten-Design für familiengeführten Weinbaubetrieb
Zielgruppe
Wir sind ein Familiengeführter Weinbaubetrieb und vermarkten unseren Wein in 0,75l Flaschen sowie auch Säfte und Schnäpse.
Zur zeit Verkaufen wir unseren Wein an Gastro und Private Kunden auch teils über Messen
Aufgabenstellung
Das derzeitige Etikett ist recht schlicht gestaltet und das Logo besteht rein aus dem geschriebenen Namen Winzerhof Dolmeck. Es kann aber auch gerne nur mit dem Namen Dolmeck ohne Winzerhof gearbeitet werden! Mit dem einbringen einer neuen Generation in den Betrieb wollen wir das aussehen unserer Produkte erneuern. Dazu kann sich gerne mit dem Namen als 'Logo' in jeglicher Art gespielt werden. Wir füllen unsere Weine in 0,75l Bordeaux Flaschen. Die Form des Etikett ist kein K.O. Kriterium jedoch wurde ursprünglich ein rund um Etikett angedacht. Sollten die Designes sich auch anders realisieren lassen sind wir gerne offen für Ideen.

```html
<!DOCTYPE html>
<html lang="de">
<head>
<meta charset="utf-8">
<title>Winzerhof Dolmeck – Grüner Veltliner Etikett</title>
<link href="https://fonts.googleapis.com/css2?family=Questrial&family=Cormorant+Garamond:ital,wght@1,500&display=swap" rel="stylesheet">
<style>
  :root {
    --page: #ffffff;
    --label-light: #ffffff;
    --label-shade: #e9e9ea;
    --label-edge: #d4d4d6;
    --vine-green: #8cb91f;
    --ink: #1d1d1b;
    --vintage-red: #b8222c;
    --soft-grey: #9a9a9c;
    --grape-beige: #d9ccaa;
    --rows-grey: #b9b9bb;
  }
  html, body {
    margin: 0;
    width: 1015px;
    height: 1200px;
    overflow: hidden;
    background: var(--page);
  }
  .canvas {
    position: relative;
    width: 1015px;
    height: 1200px;
  }
  .label {
    position: absolute;
    left: 281px;
    top: 140px;
    width: 452px;
    height: 920px;
  }
  .label-shape {
    position: absolute;
    inset: 0;
  }
  .label-text {
    position: absolute;
    left: 0;
    width: 100%;
    text-align: center;
    font-family: "Questrial", sans-serif;
    color: var(--ink);
    margin: 0;
  }
  .tab-name {
    top: 42px;
    font-size: 24px;
    color: #ffffff;
    letter-spacing: 1px;
  }
  .estate-prefix {
    top: 330px;
    font-size: 24px;
    letter-spacing: 3px;
  }
  .estate-name {
    top: 362px;
    font-size: 54px;
    letter-spacing: 2px;
  }
  .vintage {
    top: 498px;
    font-family: "Cormorant Garamond", serif;
    font-style: italic;
    font-weight: 500;
    font-size: 28px;
    letter-spacing: 12px;
    color: var(--vintage-red);
  }
  .grape-mark {
    position: absolute;
    left: 206px;
    top: 540px;
    width: 38px;
    height: 56px;
    border-radius: 40% 40% 50% 50%;
    background: var(--grape-beige);
    opacity: 0.8;
  }
  .variety {
    top: 544px;
    font-size: 30px;
    line-height: 38px;
    letter-spacing: 4px;
  }
  .style {
    top: 624px;
    font-size: 15px;
    letter-spacing: 7px;
    color: var(--soft-grey);
  }
  .vineyard {
    position: absolute;
    left: 114px;
    top: 700px;
    width: 176px;
    height: 88px;
    border-radius: 6px;
    background: linear-gradient(160deg, #e4e4e5 0%, var(--rows-grey) 55%, #d6d6d7 100%);
  }
  .region {
    top: 826px;
    font-size: 17px;
    letter-spacing: 8px;
    color: var(--soft-grey);
  }
  .region small {
    font-size: 9px;
    letter-spacing: 1px;
  }
</style>
</head>
<body>
<main class="canvas">
  <section class="label" aria-label="Weinetikett Grüner Veltliner">
    <svg class="label-shape" width="452" height="920" viewBox="0 0 452 920" aria-hidden="true">
      <defs>
        <linearGradient id="labelSheen" x1="0" y1="0" x2="1" y2="0">
          <stop offset="0" stop-color="var(--label-shade)"/>
          <stop offset="0.25" stop-color="var(--label-light)"/>
          <stop offset="0.75" stop-color="var(--label-light)"/>
          <stop offset="1" stop-color="var(--label-shade)"/>
        </linearGradient>
      </defs>
      <path class="label-body"
            d="M14,82 H96 L200,212 Q226,244 252,212 L356,82 H438 Q452,82 452,96 V850 L226,916 L0,850 V96 Q0,82 14,82 Z"
            fill="url(#labelSheen)" stroke="var(--label-edge)" stroke-width="1.5"/>
      <path class="label-tab"
            d="M120,0 H332 Q350,0 340,14 L242,120 Q226,138 210,120 L112,14 Q102,0 120,0 Z"
            fill="var(--vine-green)"/>
    </svg>

    <p class="label-text tab-name">Dolmeck</p>

    <p class="label-text estate-prefix">Winzerhof</p>
    <p class="label-text estate-name">Dolmeck</p>

    <p class="label-text vintage">2021</p>
    <div class="grape-mark" role="img" aria-label="Kleine Weintrauben-Illustration"></div>
    <h1 class="label-text variety">GRÜNER<br>VELTLINER</h1>
    <p class="label-text style">trocken</p>

    <div class="vineyard" role="img" aria-label="Illustration von Rebzeilen im Weingarten"></div>

    <p class="label-text region">WEINVIERTEL <small>DAC</small></p>
  </section>
</main>
</body>
</html>
```